fizzy drinks label design

I want to design fizzy drink label for 3 flavors : black grapes, red apple and mojito, band name kestrola, product name KOLTA , product will be in plastic bottle, label size 198 mm X 66mm

```html
<!DOCTYPE html>
<html lang="en">
<head>
<meta charset="utf-8">
<title>KOLTA fizzy drink labels</title>
<link rel="stylesheet" href="https://fonts.googleapis.com/css2?family=Montserrat:wght@400;600;700;800;900&family=Roboto+Condensed:wght@400;700&display=swap">
<style>
  :root {
    --page: #dedede;
    --white: #ffffff;
    --apple-bg: #050505;
    --apple-red: #e31e24;
    --grape-light: #f6a200;
    --grape-dark: #ea5f0f;
    --grape-ink: #0c0c0c;
    --mojito-green: #0b9a3c;
    --mojito-lime: #d7e100;
    --mojito-deep: #0b6a2c;
    --mojito-yellow: #ffe900;
    --badge-green: #2aa339;
    --badge-red: #e31e24;
    --text-font: "Montserrat", sans-serif;
    --cond-font: "Roboto Condensed", sans-serif;
  }
  * { box-sizing: border-box; margin: 0; padding: 0; }
  html, body { width: 1200px; height: 1200px; overflow: hidden; background: var(--page); }
  .label-sheet {
    width: 1200px; height: 1200px;
    display: flex; flex-direction: column; align-items: center; justify-content: center; gap: 40px;
  }
  .label {
    position: relative; width: 1000px; height: 334px; overflow: hidden;
    font-family: var(--text-font); color: var(--white);
    box-shadow: 0 4px 10px rgba(0,0,0,.18);
  }
  .label--apple { --bg: var(--apple-bg); --brand: var(--apple-red); --swoosh: var(--apple-red); --band: var(--apple-bg); --mark: var(--white); --badge: var(--badge-green); --fruit: radial-gradient(circle at 45% 40%, #ee2a2f, #d8161c 70%); background: var(--apple-bg); }
  .label--grape { --brand: var(--grape-ink); --swoosh: var(--apple-red); --band: var(--apple-red); --mark: var(--grape-ink); --badge: var(--badge-green); --fruit: radial-gradient(circle at 50% 45%, #1c1c1c, #000 75%); background: linear-gradient(90deg, var(--grape-dark) 0%, var(--grape-light) 50%, var(--grape-dark) 100%); }
  .label--mojito { --brand: var(--mojito-yellow); --swoosh: var(--mojito-deep); --band: var(--mojito-deep); --mark: var(--mojito-deep); --badge: var(--badge-red); --fruit: radial-gradient(circle at 45% 45%, #f3f7b0, #c8dc5a 55%, #4f9a3a 95%); background: linear-gradient(180deg, var(--mojito-green) 0%, #7dc321 50%, var(--mojito-lime) 100%); }

  .swoosh { position: absolute; left: 0; top: 0; width: 336px; height: 334px; }
  .swoosh path { fill: var(--swoosh); }

  .flavour-band {
    position: absolute; bottom: 0; width: 26px; height: 150px; background: var(--band);
    display: flex; align-items: center; justify-content: center;
  }
  .flavour-band--front { left: 10px; }
  .flavour-band--back { left: 634px; }
  .flavour-band span {
    transform: rotate(-90deg); white-space: nowrap;
    font-family: var(--cond-font); font-size: 19px; color: var(--white);
  }

  .brand-name { position: absolute; font-weight: 900; color: var(--brand); letter-spacing: 2px; line-height: 1; }
  .brand-name--side { left: 40px; top: 58px; font-size: 70px; }
  .brand-name--front { left: 350px; top: 36px; font-size: 92px; }
  .tagline { position: absolute; font-weight: 700; color: var(--white); white-space: nowrap; }
  .tagline--side { left: 105px; top: 132px; font-size: 14px; }
  .tagline--front { left: 420px; top: 134px; font-size: 15px; }

  .maker-name { position: absolute; font-weight: 800; color: var(--mark); line-height: 1; }
  .maker-name--side { left: 150px; top: 260px; font-size: 36px; }
  .maker-name--back { left: 692px; top: 44px; font-size: 25px; color: var(--white); }

  .veg-mark { position: absolute; left: 630px; top: 22px; width: 22px; height: 22px; background: var(--white); border: 3px solid var(--badge-green); }

  .fruit-art { position: absolute; background: var(--fruit); }
  .label--apple .fruit-art { left: 392px; top: 165px; width: 232px; height: 200px; border-radius: 48% 48% 40% 40%; }
  .label--grape .fruit-art { left: 430px; top: 158px; width: 150px; height: 170px; border-radius: 45% 45% 50% 50%; }
  .label--mojito .fruit-art { left: 405px; top: 178px; width: 210px; height: 150px; border-radius: 50%; }

  .lab-badge {
    position: absolute; width: 54px; height: 54px; border-radius: 50%;
    background: var(--badge); border: 3px solid var(--white);
  }
  .label--apple .lab-badge, .label--mojito .lab-badge { left: 566px; top: 152px; }
  .label--grape .lab-badge { left: 358px; top: 175px; }

  .net-volume { position: absolute; left: 346px; top: 290px; font-family: var(--cond-font); line-height: 1; color: var(--white); }
  .net-volume small { display: block; font-size: 10px; }
  .net-volume strong { font-size: 17px; font-weight: 400; }
  .label--grape .net-volume { color: var(--white); }

  .code-panel { position: absolute; left: 697px; top: 97px; width: 122px; height: 102px; background: var(--white); }

  .bin-icon { position: absolute; left: 770px; top: 210px; width: 36px; height: 44px; }
  .bin-icon * { fill: var(--white); }

  .nutrition {
    position: absolute; left: 828px; top: 40px; width: 143px; height: 218px;
    border: 2px solid var(--white); padding: 4px 6px; font-size: 11px; line-height: 1.35;
  }
  .nutrition h3 { font-size: 13px; font-weight: 700; }
  .nutrition .row { border-top: 1px solid var(--white); padding-top: 1px; margin-top: 2px; }
  .nutrition .row--thick { border-top-width: 3px; }
  .nutrition .right { text-align: right; }
  .nutrition b { font-weight: 700; }
  .nutrition .note { font-size: 7px; }

  .fine-print {
    position: absolute; left: 686px; top: 272px; width: 290px;
    font-family: var(--cond-font); font-size: 9.6px; line-height: 1.3; color: var(--white);
  }
</style>
</head>
<body>
<main class="label-sheet">

  <section class="label label--apple" aria-label="Red apple label">
    <svg class="swoosh" viewBox="0 0 336 334" aria-hidden="true">
      <path d="M0 28 C22 16 46 10 72 10 C42 18 20 28 0 44 Z"/>
      <path d="M28 334 C62 236 150 176 332 166 L332 172 C172 184 94 244 62 334 Z"/>
      <path d="M78 334 C104 262 150 218 232 196 C168 228 126 272 108 334 Z"/>
      <path d="M336 174 C318 222 312 282 318 334 L336 334 Z"/>
    </svg>
    <div class="flavour-band flavour-band--front"><span>RED APPLE</span></div>
    <div class="brand-name brand-name--side">KOLTA</div>
    <div class="tagline tagline--side">Apple based fizzy drink</div>
    <div class="maker-name maker-name--side">kestrola</div>

    <div class="brand-name brand-name--front">KOLTA</div>
    <div class="tagline tagline--front">Apple based fizzy drink</div>
    <div class="veg-mark"></div>
    <div class="fruit-art" role="img" aria-label="Illustration of a red apple"></div>
    <div class="lab-badge"></div>
    <div class="net-volume"><small>NET VOL.</small><strong>250ml</strong></div>
    <div class="flavour-band flavour-band--back"><span>RED APPLE</span></div>

    <div class="maker-name maker-name--back">kestrola</div>
    <div class="code-panel"></div>
    <svg class="bin-icon" viewBox="0 0 36 44" aria-hidden="true"><circle cx="26" cy="5" r="4"/><path d="M22 11 L30 11 L33 30 L36 44 L31 44 L28 32 L25 44 L21 44 Z"/><rect x="0" y="18" width="20" height="3"/><path d="M2 23 L18 23 L16 44 L4 44 Z"/></svg>
    <div class="nutrition">
      <h3>Nutritional Facts</h3>
      <div>Serving size xxxxx</div>
      <div class="row">Amount Per Serving</div>
      <div><b>Calories 120</b></div>
      <div class="row row--thick right">% Daily Value*</div>
      <div class="row"><b>Total Fat</b> 0g</div>
      <div class="row"><b>Sodium</b> 50mg</div>
      <div class="row"><b>Sugar</b> 30g</div>
      <div class="row row--thick"><b>Protein</b> 0g</div>
      <div class="row note">*Sample text</div>
    </div>
    <p class="fine-print">Lorem ipsum dolor sit amet, consectetuer adipiscing elit, sed diam nonummy nibh euismod tincidunt ut laoreet dolore magna aliquam erat Lorem ipsum dolor sit amet, consectetuer adipiscing elit, sed diam nonummy nibh euismod tincidunt ut laoreet dolore magna</p>
  </section>

  <section class="label label--grape" aria-label="Black grapes label">
    <svg class="swoosh" viewBox="0 0 336 334" aria-hidden="true">
      <path d="M0 28 C22 16 46 10 72 10 C42 18 20 28 0 44 Z"/>
      <path d="M28 334 C62 236 150 176 332 166 L332 172 C172 184 94 244 62 334 Z"/>
      <path d="M78 334 C104 262 150 218 232 196 C168 228 126 272 108 334 Z"/>
      <path d="M336 174 C318 222 312 282 318 334 L336 334 Z"/>
    </svg>
    <div class="flavour-band flavour-band--front"><span>BLACK GRAPES</span></div>
    <div class="brand-name brand-name--side">KOLTA</div>
    <div class="tagline tagline--side">Grape based fizzy drink</div>
    <div class="maker-name maker-name--side">kestrola</div>

    <div class="brand-name brand-name--front">KOLTA</div>
    <div class="tagline tagline--front">Grape based fizzy drink</div>
    <div class="veg-mark"></div>
    <div class="fruit-art" role="img" aria-label="Illustration of a bunch of black grapes"></div>
    <div class="lab-badge"></div>
    <div class="net-volume"><small>NET VOL.</small><strong>250ml</strong></div>
    <div class="flavour-band flavour-band--back"><span>BLACK GRAPES</span></div>

    <div class="maker-name maker-name--back">kestrola</div>
    <div class="code-panel"></div>
    <svg class="bin-icon" viewBox="0 0 36 44" aria-hidden="true"><circle cx="26" cy="5" r="4"/><path d="M22 11 L30 11 L33 30 L36 44 L31 44 L28 32 L25 44 L21 44 Z"/><rect x="0" y="18" width="20" height="3"/><path d="M2 23 L18 23 L16 44 L4 44 Z"/></svg>
    <div class="nutrition">
      <h3>Nutritional Facts</h3>
      <div>Serving size xxxxx</div>
      <div class="row">Amount Per Serving</div>
      <div><b>Calories 120</b></div>
      <div class="row row--thick right">% Daily Value*</div>
      <div class="row"><b>Total Fat</b> 0g</div>
      <div class="row"><b>Sodium</b> 50mg</div>
      <div class="row"><b>Sugar</b> 30g</div>
      <div class="row row--thick"><b>Protein</b> 0g</div>
      <div class="row note">*Sample text</div>
    </div>
    <p class="fine-print">Lorem ipsum dolor sit amet, consectetuer adipiscing elit, sed diam nonummy nibh euismod tincidunt ut laoreet dolore magna aliquam erat Lorem ipsum dolor sit amet, consectetuer adipiscing elit, sed diam nonummy nibh euismod tincidunt ut laoreet dolore magna</p>
  </section>

  <section class="label label--mojito" aria-label="Mojito label">
    <svg class="swoosh" viewBox="0 0 336 334" aria-hidden="true">
      <path d="M0 28 C22 16 46 10 72 10 C42 18 20 28 0 44 Z"/>
      <path d="M28 334 C62 236 150 176 332 166 L332 172 C172 184 94 244 62 334 Z"/>
      <path d="M78 334 C104 262 150 218 232 196 C168 228 126 272 108 334 Z"/>
      <path d="M336 174 C318 222 312 282 318 334 L336 334 Z"/>
    </svg>
    <div class="flavour-band flavour-band--front"><span>MOJITO</span></div>
    <div class="brand-name brand-name--side">KOLTA</div>
    <div class="tagline tagline--side">Mojito based fizzy drink</div>
    <div class="maker-name maker-name--side">kestrola</div>

    <div class="brand-name brand-name--front">KOLTA</div>
    <div class="tagline tagline--front">Mojito based fizzy drink</div>
    <div class="veg-mark"></div>
    <div class="fruit-art" role="img" aria-label="Photo of lime halves with mint leaves"></div>
    <div class="lab-badge"></div>
    <div class="net-volume"><small>NET VOL.</small><strong>250ml</strong></div>
    <div class="flavour-band flavour-band--back"><span>MOJITO</span></div>

    <div class="maker-name maker-name--back">kestrola</div>
    <div class="code-panel"></div>
    <svg class="bin-icon" viewBox="0 0 36 44" aria-hidden="true"><circle cx="26" cy="5" r="4"/><path d="M22 11 L30 11 L33 30 L36 44 L31 44 L28 32 L25 44 L21 44 Z"/><rect x="0" y="18" width="20" height="3"/><path d="M2 23 L18 23 L16 44 L4 44 Z"/></svg>
    <div class="nutrition">
      <h3>Nutritional Facts</h3>
      <div>Serving size xxxxx</div>
      <div class="row">Amount Per Serving</div>
      <div><b>Calories 120</b></div>
      <div class="row row--thick right">% Daily Value*</div>
      <div class="row"><b>Total Fat</b> 0g</div>
      <div class="row"><b>Sodium</b> 50mg</div>
      <div class="row"><b>Sugar</b> 30g</div>
      <div class="row row--thick"><b>Protein</b> 0g</div>
      <div class="row note">*Sample text</div>
    </div>
    <p class="fine-print">Lorem ipsum dolor sit amet, consectetuer adipiscing elit, sed diam nonummy nibh euismod tincidunt ut laoreet dolore magna aliquam erat Lorem ipsum dolor sit amet, consectetuer adipiscing elit, sed diam nonummy nibh euismod tincidunt ut laoreet dolore magna</p>
  </section>

</main>
</body>
</html>
```